We need a complete design for our construction company KELMO CONSTRUCTION based in Auckland New Zealand, we need a logo, website, business card, vehicle design etc..
We are a mid to high-end construction company who work mostly on residential projects and some commercial.

What we want to see in the design;
Professional,
Architectural,
Simple,
Alternative,

We want the design to communicate professionalism, high quality wormanship and and quality service.

Target Market(s)

People looking for a quality building/ construction company

Industry/Entity Type

Construction Company

Contact Information for Business Card

KELMO CONSTRUCTION.co.nz
Teo Vrankel
teo@kelmoconstruction.example.nz
021 5873 406

Logo Text

KELMO CONSTRUCTION

Number of Pages Required

5+ page

Font styles to use
Sans Serif

Colors

Designer to choose colors to be used in the design.

Requirements
Must have
• Must appear high end, professional, quality, be simple, easy to use, give security to potential clients
Nice to have
• high-quality photos of our recent projects
• about us page
• blog page
• contact us page
• high quality content
Should not have
• should not be hard to use and have too much going on.

```html
<!DOCTYPE html>
<html lang="en">
<head>
<meta charset="utf-8">
<title>KELMO CONSTRUCTION — Home</title>
<link rel="stylesheet" href="https://fonts.googleapis.com/css2?family=Montserrat:wght@300;400;500;600;700&family=Libre+Baskerville&display=swap">
<style>
:root{
  --accent:#f5a716;
  --ink:#16181c;
  --muted:#7d828a;
  --line:#d7dadf;
  --page:#eef0f3;
  --white:#ffffff;
  --link:#2b9bd3;
  --star:#6fb72c;
}
*{box-sizing:border-box;margin:0;padding:0}
html,body{width:1200px;height:3622px;overflow:hidden}
body{position:relative;background:var(--page);font-family:"Montserrat",sans-serif;color:var(--ink)}
.abs{position:absolute}

/* header */
.site-header{left:0;top:0;width:1200px;height:88px;background:var(--white)}
.brand{left:85px;top:22px;display:flex;align-items:center;gap:10px}
.brand-mark{width:22px;height:22px;background:var(--accent)}
.brand-name{font-size:20px;font-weight:700;color:var(--accent);letter-spacing:1px;line-height:1}
.brand-sub{font-size:10px;font-weight:500;letter-spacing:3px;color:var(--accent)}
.main-nav{left:379px;top:36px;display:flex;gap:46px;font-size:14px;font-weight:500}
.main-nav .active{color:var(--accent)}
.quote-btn{left:961px;top:0;width:104px;height:88px;background:var(--accent);font-size:13px;font-weight:700;text-align:center;display:flex;align-items:center;justify-content:center;line-height:1.2}

/* hero */
.blueprint{left:700px;top:88px;width:500px;height:560px;background:radial-gradient(circle at 60% 40%,rgba(200,205,212,.45),rgba(238,240,243,0) 70%)}
.hero-kicker{left:99px;top:224px;font-size:16px;line-height:1.5;width:260px}
.hero-kicker b{color:var(--accent);font-weight:500}
.hero-title{left:99px;top:306px;font-size:62px;font-weight:700;line-height:70px}

/* main card */
.main-card{left:97px;top:628px;width:1004px;height:2711px;background:var(--white);border-top:7px solid var(--accent);border-bottom:7px solid var(--accent)}
.section-title{font-size:20px;font-weight:700;line-height:28px;border-left:4px solid var(--accent);padding-left:20px}

.intro-frame{left:186px;top:715px;width:348px;height:453px;border:2px solid var(--line);padding:22px}
.photo{width:100%;height:100%}
.photo-tower{background:linear-gradient(180deg,#5b7ea8 0%,#33465f 55%,#1e2734 100%)}
.intro-title{left:616px;top:715px}
.intro-lead{left:616px;top:826px;width:392px;font-size:15px;font-weight:700;line-height:21px}
.intro-text{left:616px;top:920px;width:392px;font-size:12.5px;line-height:21px;color:var(--muted)}
.intro-text a{color:var(--link);font-weight:700}
.read-more{left:616px;top:1073px;font-size:12px;font-weight:700;color:var(--link)}

.stat{top:1205px;font-weight:300}
.stat-num{font-size:42px;line-height:48px}
.stat-label{font-size:13px;line-height:18px;color:var(--muted);margin-top:6px}

.spec-title{left:121px;top:1376px}
.spec-card{top:1487px;width:228px;height:196px;border:2px solid var(--line);padding:24px 20px}
.spec-head{display:flex;gap:14px;align-items:flex-start}
.spec-head svg{flex:none}
.spec-name{font-size:15px;font-weight:700;line-height:18px}
.spec-desc{margin-top:20px;font-size:12px;line-height:20px;color:var(--muted)}

.proj-title{left:121px;top:1750px}
.view-all{left:939px;top:1772px;font-size:12px;color:var(--link);font-weight:500}

.tile{position:absolute}
.tile span{position:absolute;left:38px;bottom:10px;font-size:12px;color:var(--white)}
.t1{left:87px;top:1859px;width:514px;height:514px;background:linear-gradient(180deg,#3a5f8c 0%,#8a9bb0 50%,#3a3128 100%)}
.t2{left:601px;top:1859px;width:512px;height:261px;background:linear-gradient(180deg,#1f3f7a 0%,#4b6aa0 55%,#c49b5a 100%)}
.t3{left:601px;top:2120px;width:256px;height:253px;background:linear-gradient(180deg,#5b8fc9 0%,#8b8e86 60%,#3b3a2e 100%)}
.t4{left:857px;top:2120px;width:256px;height:253px;background:linear-gradient(180deg,#8db6dd 0%,#d9dbd8 55%,#6a7b5a 100%)}
.t2 span,.t3 span,.t4 span{left:38px}

/* testimonial */
.trust-title{left:180px;top:2487px;width:259px;text-align:right;border-left:0;border-right:4px solid var(--accent);padding:0 22px 0 0}
.score{left:180px;top:2600px;width:262px;text-align:right;font-size:62px;font-weight:300}
.stars{left:302px;top:2688px;display:flex;gap:3px}
.see-review{left:180px;top:2735px;width:262px;text-align:right;font-size:11px;color:var(--muted)}
.rater{left:180px;top:2752px;width:262px;text-align:right;font-size:12px;color:var(--muted);display:flex;justify-content:flex-end;align-items:center;gap:10px}
.rater i{width:10px;height:10px;background:var(--accent);display:block}
.quote{left:150px;top:2818px;width:292px;text-align:right;font-family:"Libre Baskerville",serif;font-size:28px;line-height:36px}
.author{left:180px;top:3027px;width:262px;text-align:right;font-size:12px;color:var(--muted)}

.post-card{left:541px;top:2487px;width:471px;height:528px;border:2px solid var(--line);padding:22px}
.photo-stadium{height:344px;background:linear-gradient(180deg,#3a6fb0 0%,#9fb6cc 45%,#e6e8e8 60%,#2e5677 100%)}
.meta{font-size:10px;color:var(--muted);display:flex;gap:14px}
.post-title{font-size:20px;font-weight:700;line-height:24px}
.more{font-size:11px;color:var(--link);font-weight:500}
.post-card .meta{margin-top:22px}
.post-card .post-title{margin-top:18px}
.post-card .more{margin-top:24px}

.mini-posts{left:541px;top:3042px;width:471px;height:181px;border:2px solid var(--line);border-left:5px solid var(--accent);display:flex;padding:18px 20px 0 20px;gap:30px}
.mini{width:195px}
.mini .post-title{font-size:15px;line-height:20px;margin-top:18px}
.mini .more{margin-top:20px}

/* footer */
.site-footer{left:0;top:3505px;width:1200px;height:117px;background:var(--white)}
.copyright{left:0;width:1200px;top:52px;text-align:center;font-size:12px}
.social{left:880px;top:50px;display:flex;gap:16px;font-size:12px;font-weight:600}
</style>
</head>
<body>

<header class="abs site-header">
  <div class="abs brand">
    <span class="brand-mark"></span>
    <div>
      <div class="brand-name">KELMO</div>
      <div class="brand-sub">CONSTRUCTION</div>
    </div>
  </div>
  <nav class="abs main-nav">
    <span class="active">Home</span><span>Works</span><span>News</span><span>Blog</span><span>About</span><span>Contact</span>
  </nav>
  <div class="abs quote-btn">GET A<br>QUOTE</div>
</header>

<div class="abs blueprint" role="img" aria-label="Faint architectural blueprint drawing in the background"></div>
<p class="abs hero-kicker">We're <b>VARDO</b> Construction and Development</p>
<h1 class="abs hero-title">Perfection is<br>always<br>under constuction</h1>

<main class="abs main-card"></main>

<div class="abs intro-frame"><div class="photo photo-tower" role="img" aria-label="Photo of a glass office tower at dusk"></div></div>
<h2 class="abs section-title intro-title">Introduce about<br>Vardo</h2>
<p class="abs intro-lead">Founded in Lebanon in 1967, Vardo Construction Company (VCC) has grown to become one of the Middle East's leading construction contractors.</p>
<p class="abs intro-text">We specialise in complex and prestigious construction and infrastructure projects. Our portfolio includes some of the region's most iconic landmarks, from super high-rise luxury developments, to five star <a>HOTELS</a>, hospitals and intricately sophisticated smart buildings. We have exacting HSE and sustainability standards and the health and safety of both our employees and the general public is given utmost priority.</p>
<a class="abs read-more">READ MORE</a>

<div class="abs stat" style="left:616px"><div class="stat-num">24</div><div class="stat-label">Years<br>Experience</div></div>
<div class="abs stat" style="left:746px"><div class="stat-num">865</div><div class="stat-label">Projects<br>Completed</div></div>
<div class="abs stat" style="left:876px"><div class="stat-num">4200</div><div class="stat-label">Workers<br>Employed</div></div>

<h2 class="abs section-title spec-title">Our Speciality<br>Include</h2>

<div class="abs spec-card" style="left:109px">
  <div class="spec-head">
    <svg width="24" height="26" viewBox="0 0 24 26" fill="none" stroke="#8a8f96" stroke-width="1.6"><rect x="2" y="4" width="11" height="20"/><rect x="13" y="10" width="9" height="14"/><path d="M5 9h5M5 13h5M5 17h5M16 15h3M16 19h3"/></svg>
    <div class="spec-name">Design &amp;<br>Construction</div>
  </div>
  <p class="spec-desc">Construction of all types of buildings, infrastructure and civil works construction</p>
</div>
<div class="abs spec-card" style="left:360px">
  <div class="spec-head">
    <svg width="24" height="24" viewBox="0 0 24 24" fill="none" stroke="#8a8f96" stroke-width="1.6"><path d="M12 3l9 5-9 5-9-5z"/><path d="M3 12l9 5 9-5M3 16l9 5 9-5"/></svg>
    <div class="spec-name">Rennovation &amp;<br>Reconstruction</div>
  </div>
  <p class="spec-desc">We're offer reconstruction &amp; rennovation service for any types of buildings.</p>
</div>
<div class="abs spec-card" style="left:611px">
  <div class="spec-head">
    <svg width="24" height="24" viewBox="0 0 24 24" fill="none" stroke="#8a8f96" stroke-width="1.6"><rect x="3" y="3" width="18" height="18"/><path d="M7 17v-5M11 17V8M15 17v-7"/></svg>
    <div class="spec-name">Turnkey<br>Contracting</div>
  </div>
  <p class="spec-desc">We offer full contracting services and have the flexibility to assist our clients</p>
</div>
<div class="abs spec-card" style="left:864px">
  <div class="spec-head">
    <svg width="24" height="24" viewBox="0 0 24 24" fill="#8a8f96"><circle cx="12" cy="12" r="7"/><circle cx="12" cy="12" r="3" fill="#fff"/><rect x="10.5" y="1" width="3" height="5"/><rect x="10.5" y="18" width="3" height="5"/><rect x="1" y="10.5" width="5" height="3"/><rect x="18" y="10.5" width="5" height="3"/></svg>
    <div class="spec-name">Equipment<br>Installation</div>
  </div>
  <p class="spec-desc">We offer equipment removal &amp; installaion service with quality &amp; quickly process</p>
</div>

<h2 class="abs section-title proj-title">Projects That We<br>Completed</h2>
<a class="abs view-all">VIEW ALL PROJECT</a>

<div class="tile t1" role="img" aria-label="Photo of a curved museum building at dusk"><span>Buildings</span></div>
<div class="tile t2" role="img" aria-label="Photo of a flowing white cultural centre at night"><span>Commercials</span></div>
<div class="tile t3" role="img" aria-label="Photo of a modern concrete house with garden"><span>Commercials</span></div>
<div class="tile t4" role="img" aria-label="Photo of a white apartment building with terraces"><span>Buildings</span></div>

<h2 class="abs section-title trust-title">Trusted From Our<br>Clients</h2>
<div class="abs score">9.5</div>
<svg class="abs stars" width="140" height="24" viewBox="0 0 140 24" style="left:302px;top:2688px">
  <g fill="var(--star)">
    <path d="M12 1l3.3 7 7.7.8-5.8 5.2 1.7 7.6L12 17.8 5.1 21.6l1.7-7.6L1 8.8 8.7 8z"/>
    <path transform="translate(28)" d="M12 1l3.3 7 7.7.8-5.8 5.2 1.7 7.6L12 17.8 5.1 21.6l1.7-7.6L1 8.8 8.7 8z"/>
    <path transform="translate(56)" d="M12 1l3.3 7 7.7.8-5.8 5.2 1.7 7.6L12 17.8 5.1 21.6l1.7-7.6L1 8.8 8.7 8z"/>
    <path transform="translate(84)" d="M12 1l3.3 7 7.7.8-5.8 5.2 1.7 7.6L12 17.8 5.1 21.6l1.7-7.6L1 8.8 8.7 8z"/>
    <path transform="translate(112)" d="M12 1v16.8L5.1 21.6l1.7-7.6L1 8.8 8.7 8z"/>
  </g>
</svg>
<div class="abs see-review">See review here</div>
<div class="abs rater"><i></i>RATENEST</div>
<blockquote class="abs quote">Excellent service, efficient and left everywhere spotless ! Thank you</blockquote>
<div class="abs author">- Lena Harwick</div>

<article class="abs post-card">
  <div class="photo-stadium" role="img" aria-label="Photo of a curved glass hotel reflected in a pool"></div>
  <div class="meta"><span>February 15, 2018</span><span>•</span><span>vardo</span></div>
  <h3 class="post-title">New Policy For Protect Workers In Contruction Industrial</h3>
  <div class="more">FULL ARTICLE &nbsp;›</div>
</article>

<div class="abs mini-posts">
  <article class="mini">
    <div class="meta"><span>February 15, 2018</span><span>•</span><span>vardo</span></div>
    <h3 class="post-title">Morroco Shopping Center By VARDO</h3>
    <div class="more">FULL ARTICLE &nbsp;›</div>
  </article>
  <article class="mini">
    <div class="meta"><span>February 15, 2018</span><span>•</span><span>vardo</span></div>
    <h3 class="post-title">Discover Wood's Struture From NAH Park, Germany</h3>
    <div class="more">FULL ARTICLE &nbsp;›</div>
  </article>
</div>

<footer class="abs site-footer">
  <p class="abs copyright">© 2018 Vardo. All Right Reserved</p>
  <div class="abs social"><span>Threadly</span><span>Chirpo</span><span>Plusto</span><span>Streamo</span></div>
</footer>

</body>
</html>
```